Building company buisness cards

We are looking for a sharp modern new look for our business cards.We are a New Zealand based company that specialises in house and land packages.We have attached a photo of the current logo and would like to see if it can be improved somehow if needed.We are open to any colours but we have chosen Black and White at this stage. Feel free to change the font and make the logo smarter looking.Play with the colours and see what looks best.We want a card that looks so good know one will want to throw it away!

Target Market(s)

Building profesonals, home buyers

Industry/Entity Type

Building

Contact Information for Business Card

Derek Haskins
0274930268
derekh@stonerange.co.nz

Font styles to use
Serif
Sans Serif

Colors

Designer to choose colors to be used in the design.

Requirements
Must have
• Just the logo on one side and details on the other
• Clean simple looking card
Nice to have
• Round corners and detail like raised or spot UV
• Something that stands out
Should not have
• To title needed, Director etc

```html
<!DOCTYPE html>
<html lang="en">
<head>
<meta charset="utf-8">
<title>Stonerange Business Cards</title>
<link href="https://fonts.googleapis.com/css2?family=Playfair+Display:wght@700&family=Montserrat:wght@300;400&family=Oswald:wght@500&display=swap" rel="stylesheet">
<style>
  :root {
    --backdrop: #1c1c1c;
    --card: #141414;
    --card-edge: #0c0c0c;
    --silver: #d4d4d4;
    --silver-dim: #8a8a8a;
    --gloss: #3a3a3a;
    --text-muted: #9a9a9a;
  }
  * { margin: 0; padding: 0; box-sizing: border-box; }
  html, body {
    width: 1200px;
    height: 900px;
    overflow: hidden;
    background: var(--backdrop);
  }
  .sheet {
    width: 1200px;
    height: 900px;
    display: flex;
    align-items: center;
    justify-content: center;
    gap: 40px;
  }
  .card {
    position: relative;
    width: 540px;
    height: 310px;
    background: var(--card);
    border-radius: 10px;
    box-shadow: 0 0 0 1px var(--card-edge), 0 18px 40px rgba(0,0,0,0.55);
    overflow: hidden;
  }

  /* Front: brand */
  .card-front {
    display: flex;
    align-items: center;
    justify-content: center;
  }
  .brand {
    display: flex;
    flex-direction: column;
    align-items: flex-start;
  }
  .brand-name {
    font-family: "Playfair Display", serif;
    font-weight: 700;
    font-size: 58px;
    line-height: 1;
    color: var(--silver);
    letter-spacing: 0.5px;
  }
  .tagline {
    margin-top: 8px;
    font-family: "Montserrat", sans-serif;
    font-weight: 300;
    font-size: 17px;
    color: var(--gloss);
    letter-spacing: 0.3px;
  }

  /* Back: contact */
  .ring {
    position: absolute;
    left: 150px;
    top: 25px;
    width: 260px;
    height: 260px;
  }
  .contact {
    position: absolute;
    left: 150px;
    top: 25px;
    width: 260px;
    height: 260px;
    display: flex;
    flex-direction: column;
    align-items: center;
    justify-content: center;
  }
  .contact-name {
    font-family: "Oswald", sans-serif;
    font-weight: 500;
    font-size: 24px;
    letter-spacing: 1.5px;
    text-transform: uppercase;
    color: var(--silver-dim);
    padding-bottom: 6px;
    border-bottom: 1.5px solid var(--silver-dim);
  }
  .contact-icons {
    margin-top: 20px;
    display: flex;
    gap: 6px;
  }
  .contact-line {
    margin-top: 8px;
    font-family: "Montserrat", sans-serif;
    font-weight: 400;
    font-size: 12.5px;
    color: var(--text-muted);
    letter-spacing: 0.4px;
  }
</style>
</head>
<body>
  <main class="sheet">
    <section class="card card-front" aria-label="Card front">
      <div class="brand">
        <span class="brand-name">Stonerange</span>
        <span class="tagline">Houses shaped for living.</span>
      </div>
    </section>

    <section class="card card-back" aria-label="Card back">
      <svg class="ring" viewBox="0 0 260 260" aria-hidden="true">
        <defs>
          <linearGradient id="ringSheen" x1="0" y1="0" x2="1" y2="1">
            <stop offset="0" stop-color="#3a3a3a"/>
            <stop offset="0.45" stop-color="#e6e6e6"/>
            <stop offset="0.7" stop-color="#f5f5f5"/>
            <stop offset="1" stop-color="#6a6a6a"/>
          </linearGradient>
        </defs>
        <circle cx="130" cy="130" r="124" fill="none" stroke="url(#ringSheen)" stroke-width="8"/>
      </svg>
      <div class="contact">
        <span class="contact-name">Derek Haskins</span>
        <span class="contact-icons">
          <svg width="11" height="12" viewBox="0 0 11 12" aria-label="Phone" role="img">
            <rect x="2.5" y="0.75" width="6" height="10.5" rx="1" fill="none" stroke="#9a9a9a" stroke-width="1"/>
            <line x1="4.5" y1="9.5" x2="6.5" y2="9.5" stroke="#9a9a9a" stroke-width="1"/>
          </svg>
          <svg width="14" height="12" viewBox="0 0 14 12" aria-label="Email" role="img">
            <rect x="0.75" y="1.75" width="12.5" height="8.5" fill="none" stroke="#9a9a9a" stroke-width="1"/>
            <polyline points="0.75,1.75 7,7 13.25,1.75" fill="none" stroke="#9a9a9a" stroke-width="1"/>
          </svg>
        </span>
        <span class="contact-line">0274930268</span>
        <span class="contact-line">derekh@stonerange.co.nz</span>
      </div>
    </section>
  </main>
</body>
</html>
```